Help a start up law firm make an impression! - Website

We are a property development and conveyancing law firm looking for some to design our website. The initial brief is for 6 pages with scope for on-going work.

Law firms are traditionally quite conservative and we want to break the mold. We want to come across as fun and modern, while still being professional.

A good example is https://quorrantlaw.com.au/. It's professional yet modern.
Updates

Another good site I like in the same industry: https://www.tindalemarshconveyancing.com.au/

Target Market(s)

Tech savy home buyers and sellers - generally 30 to 50 years old

Industry/Entity Type

Law Firm

Coding

Coded - Design and coding required

Number of Pages Required

5+ page

Font styles to use
Other font styles liked:
• No idea

Colors
f04a50

Requirements
Must have
• The elements set out in the design brief document

```html
<!DOCTYPE html>
<html lang="en">
<head>
<meta charset="utf-8">
<title>Harcourt Law</title>
<link rel="stylesheet" href="https://fonts.googleapis.com/css2?family=Abril+Fatface&family=Open+Sans:ital,wght@0,400;0,600;1,400&family=Raleway:wght@500;700&display=swap">
<style>
:root{
  --rose:#d6435b;
  --rose-dark:#b9364c;
  --ink:#1a1a1a;
  --text:#555;
  --muted:#8a8a8a;
  --light:#f0f0f0;
  --night:#1e1e22;
  --white:#fff;
}
*{box-sizing:border-box;margin:0;padding:0}
html,body{width:1200px;height:3659px;overflow:hidden}
body{font-family:"Open Sans",Arial,sans-serif;color:var(--text);background:var(--white);position:relative}
.display{font-family:"Abril Fatface",Georgia,serif;font-weight:400}
.accent{color:var(--rose)}
.btn{display:inline-block;font-family:"Abril Fatface",Georgia,serif;letter-spacing:2px;text-transform:uppercase;font-size:20px;color:var(--white);background:var(--rose);border-radius:6px;padding:16px 28px;text-decoration:none}
.btn-outline{background:transparent;border:2px solid var(--white);font-size:17px;padding:14px 24px}

/* hero */
.hero{position:absolute;left:0;top:0;width:1200px;height:676px;background:linear-gradient(180deg,#6f86a3 0%,#4c6684 30%,#2c3f57 65%,#1c2637 100%)}
.hero .logo{position:absolute;left:75px;top:56px;font-size:40px;color:var(--white)}
.hero .phone{position:absolute;right:80px;top:12px;display:flex;align-items:center;gap:12px;font-family:"Abril Fatface",Georgia,serif;font-size:28px;color:var(--rose)}
.nav{position:absolute;left:425px;top:72px;display:flex;gap:22px;font-family:"Raleway",Arial,sans-serif;font-weight:500;font-size:16px;color:var(--white);text-transform:uppercase}
.nav .active{color:var(--rose)}
.hero-copy{position:absolute;left:0;top:270px;width:1200px;text-align:center;color:var(--white)}
.hero-copy h1{font-family:"Open Sans",Arial,sans-serif;font-weight:600;font-size:60px;line-height:74px}
.hero-copy p{font-size:28px;margin:6px 0 24px}

/* welcome */
.welcome{position:absolute;top:676px;width:1200px;height:417px;text-align:center}
.section-title{font-size:46px;color:var(--ink)}
.welcome h2{margin-top:60px}
.welcome p{width:840px;margin:18px auto 0;font-size:14px;line-height:27px;color:var(--muted)}
.welcome .btn{margin-top:22px}

/* split panels */
.split{position:absolute;width:1200px;height:397px;display:flex}
.panel{width:600px;height:397px;background:var(--rose);color:var(--white);padding:60px 72px 0 78px;position:relative}
.panel h2{font-size:40px;letter-spacing:2px;margin-bottom:16px}
.panel p{font-size:14px;line-height:25px;margin-bottom:26px}
.photo{width:600px;height:397px}
.notch{position:absolute;top:90px;width:0;height:0;border-top:26px solid transparent;border-bottom:26px solid transparent}
.conveyancing{top:1093px}
.conveyancing .notch{right:-26px;border-left:26px solid var(--rose);z-index:2}
.development{top:1886px}
.development .panel{padding-left:32px}
.development .notch{left:-26px;border-right:26px solid var(--rose)}

/* services */
.services{position:absolute;top:1490px;width:1200px;height:396px;text-align:center}
.services h2{margin-top:52px}
.service-list{display:flex;justify-content:center;gap:104px;margin-top:40px}
.service{width:164px;font-size:17px;color:#333;line-height:26px;text-transform:uppercase}
.service .disc{width:128px;height:128px;border-radius:50%;background:var(--rose);margin:0 auto 18px;display:flex;align-items:center;justify-content:center;box-shadow:0 6px 0 var(--rose-dark)}

/* blog */
.blog{position:absolute;top:2283px;width:1200px;height:572px}
.blog h2{text-align:center;margin-top:50px}
.posts{display:flex;gap:20px;margin:30px 0 0 78px}
.post{width:335px}
.post h3{font-style:italic;font-weight:400;font-size:17px;color:#333}
.tag{display:inline-block;margin:10px 0 18px;background:var(--rose);color:var(--white);font-family:"Abril Fatface",Georgia,serif;font-size:18px;padding:10px 22px;border-radius:4px}
.post .thumb{width:335px;height:160px}
.post p{font-size:13px;line-height:24px;margin-top:20px;color:var(--text)}
.arrow{display:inline-block;vertical-align:middle;margin-left:6px}

/* partners */
.partners{position:absolute;top:2855px;width:1200px;height:165px;background:var(--light);display:flex;align-items:center;justify-content:space-between;padding:0 30px}
.partner-list{display:flex;gap:74px;align-items:center}
.partner{display:flex;align-items:center;gap:10px;font-family:"Open Sans",Arial,sans-serif;font-weight:600;font-size:30px;color:#444}
.partner i{width:26px;height:26px;background:#9a9a9a;border-radius:50%}

/* contact */
.contact{position:absolute;top:3020px;width:1200px;height:575px;background:linear-gradient(180deg,#2a2b30 0%,var(--night) 100%);color:#cfcfcf}
.contact h2{font-size:32px;color:var(--white);letter-spacing:1px}
.get-started{position:absolute;left:78px;top:52px;width:636px}
.get-started p{font-size:14px;font-style:italic;line-height:25px;margin:14px 0 20px}
.field{display:flex;height:48px;background:var(--white);margin-bottom:12px;border-radius:3px;overflow:hidden}
.field .ico{width:48px;background:var(--rose);display:flex;align-items:center;justify-content:center}
.field span{padding:14px;font-size:13px;color:#999}
.row{display:flex;gap:14px}
.row .field{flex:1}
.field.tall{height:118px}
.field.tall .ico{align-items:flex-start;padding-top:14px}
.submit{height:56px;background:var(--rose);color:var(--white);font-family:"Abril Fatface",Georgia,serif;letter-spacing:3px;font-size:20px;display:flex;align-items:center;justify-content:center;border-radius:6px;margin-top:12px}
.contact-us{position:absolute;left:778px;top:52px;width:340px}
.info{display:flex;gap:18px;margin-top:20px;font-size:13px;line-height:22px}
.info:first-of-type{margin-top:24px}
.info .pin{flex:none;width:28px;height:28px;border-radius:50%;background:var(--rose);display:flex;align-items:center;justify-content:center}
.hours{display:grid;grid-template-columns:120px auto;column-gap:10px}
.socials{display:flex;gap:12px;margin-top:26px}
.socials span{width:56px;height:56px;background:var(--rose);border-radius:4px}
.footer{position:absolute;top:3595px;width:1200px;height:64px;background:var(--rose);color:var(--white);font-size:14px;display:flex;align-items:center;justify-content:center}
</style>
</head>
<body>

<header class="hero" role="img" aria-label="Photo of a city skyline with skyscrapers at dusk">
  <div class="logo display">Harcourt Law</div>
  <div class="phone">
    <svg width="36" height="36" viewBox="0 0 36 36"><circle cx="18" cy="18" r="16" fill="none" stroke="#fff" stroke-width="3"/><path d="M12 10c-2 3 1 10 6 14 3 2 5 2 6 0l-3-4-2 1c-2-1-4-4-5-6l1-2-3-3z" fill="#fff"/></svg>
    <span>1.800.555.0142</span>
  </div>
  <nav class="nav">
    <span class="active">Home</span><span>Conveyancing</span><span>Property Development</span><span>News</span><span>About Us</span><span>Contact</span>
  </nav>
  <div class="hero-copy">
    <h1>What Makes You Worry When<br><span class="accent">We Are Here ?</span></h1>
    <p>We Try Harder. We work smarter.</p>
    <a class="btn">Contact Us</a>
  </div>
</header>

<section class="welcome">
  <h2 class="section-title display">Welcome To <span class="accent">Harcourt Law</span></h2>
  <p>At Harcourt Property Group, we have a rich history of helping our clients succeed by creating high quality investment opportunities in development sites, new projects or residential properties.</p>
  <p style="margin-top:8px">We try harder. We work smarter. We avoid pitfalls by collaborating with a range of professional stakeholders who can identify lucrative building sites with strong development potential for residential and mixed-used developments. You do what you do best. At Harcourt Property Group we handle the rest.</p>
  <a class="btn">Know More</a>
</section>

<section class="split conveyancing">
  <div class="panel">
    <h2 class="display">Conveyancing</h2>
    <p>Lorem Ipsum is simply dummy text of the printing and typesetting industry. Lorem Ipsum has been the industry's standard dummy text ever since the 1500s, when an unknown printer took a galley of type and scrambled it to make a type specimen book. It has survived not only five centuries, but also the leap into electronic typesetting, rema</p>
    <a class="btn btn-outline">Know More</a>
    <span class="notch"></span>
  </div>
  <div class="photo" role="img" aria-label="Photo of a hand signing a document beside a laptop and glasses" style="background:linear-gradient(135deg,#e9ecef 0%,#c9ced4 55%,#8e959c 100%)"></div>
</section>

<section class="services">
  <h2 class="section-title display">What <span class="accent">We Do</span></h2>
  <div class="service-list">
    <div class="service"><div class="disc"><svg width="60" height="60" viewBox="0 0 60 60" fill="none" stroke="#fff" stroke-width="4"><circle cx="30" cy="30" r="24"/><path d="M18 20l20 20M38 28v12H26"/></svg></div>Cost<br>Certainty</div>
    <div class="service"><div class="disc"><svg width="60" height="60" viewBox="0 0 60 60" fill="#fff"><circle cx="20" cy="16" r="6"/><circle cx="40" cy="16" r="6"/><rect x="12" y="26" width="36" height="6"/><rect x="16" y="32" width="4" height="18"/><rect x="40" y="32" width="4" height="18"/></svg></div>Expert<br>Lawyers</div>
    <div class="service"><div class="disc"><svg width="64" height="60" viewBox="0 0 64 60" fill="none" stroke="#fff" stroke-width="4"><rect x="6" y="10" width="40" height="28" rx="2"/><path d="M18 48h16M26 38v10"/><rect x="44" y="22" width="14" height="26" rx="2"/></svg></div>Responsive<br>Service</div>
    <div class="service"><div class="disc"><svg width="60" height="60" viewBox="0 0 60 60" fill="none" stroke="#fff" stroke-width="4"><rect x="12" y="8" width="34" height="44" rx="2"/><path d="M20 20h18M20 30h18M20 40h10M48 14L34 40"/></svg></div>Commercial<br>Advice</div>
  </div>
</section>

<section class="split development">
  <div class="photo" role="img" aria-label="Photo of business people shaking hands in a bright office" style="background:linear-gradient(135deg,#dfe4ea 0%,#9aa3ad 50%,#3f454c 100%)"></div>
  <div class="panel">
    <span class="notch"></span>
    <h2 class="display">Development Law</h2>
    <p>Lorem Ipsum is simply dummy text of the printing and typesetting industry. Lorem Ipsum has been the industry's standard dummy text ever since the 1500s, when an unknown printer took a galley of type and scrambled it to make a type specimen book. It has survived not only five centuries, but also the leap into electronic typesetting, rema</p>
    <a class="btn btn-outline">Know More</a>
  </div>
</section>

<section class="blog">
  <h2 class="section-title display">Recent <span class="accent">Blog Post</span></h2>
  <div class="posts">
    <article class="post">
      <h3>Blog Post Title.</h3>
      <span class="tag">10 Sep , 2017</span>
      <div class="thumb" role="img" aria-label="Photo of colleagues meeting around a table" style="background:linear-gradient(135deg,#9a8a7a,#4e4a48)"></div>
      <p>What goes into a blog post? Helpful, industry -specific content that: 1) gives readers a useful takeaway, and 2)...<svg class="arrow" width="34" height="10" viewBox="0 0 34 10"><path d="M0 5h30M26 1l5 4-5 4" stroke="#d6435b" stroke-width="2.5" fill="none"/></svg></p>
    </article>
    <article class="post">
      <h3>Real estate laws on the move</h3>
      <span class="tag">02 July 2015</span>
      <div class="thumb" role="img" aria-label="Photo of business people standing in an office" style="background:linear-gradient(135deg,#c6ccd2,#5c636b)"></div>
      <p>Lorem Ipsum is simply dummy text of the printing and typesetting industry. Lorem Ipsum has been the industry's standard...<svg class="arrow" width="34" height="10" viewBox="0 0 34 10"><path d="M0 5h30M26 1l5 4-5 4" stroke="#d6435b" stroke-width="2.5" fill="none"/></svg></p>
    </article>
    <article class="post">
      <h3>Private equity firm takes control</h3>
      <span class="tag">02 July 2015</span>
      <div class="thumb" role="img" aria-label="Photo of executives walking together outdoors" style="background:linear-gradient(135deg,#b8c7d6,#6a6560)"></div>
      <p>Lorem Ipsum is the simply dummy text of the printing and typesetting industry. Lorem is Ipsum has been the industry's...<svg class="arrow" width="34" height="10" viewBox="0 0 34 10"><path d="M0 5h30M26 1l5 4-5 4" stroke="#d6435b" stroke-width="2.5" fill="none"/></svg></p>
    </article>
  </div>
</section>

<section class="partners" aria-label="Partners">
  <svg width="16" height="40" viewBox="0 0 16 40"><path d="M14 2L2 20l12 18" stroke="#aaa" stroke-width="2" fill="none"/></svg>
  <div class="partner-list">
    <div class="partner"><i></i>Brightfield</div>
    <div class="partner">Tallow &amp; Co</div>
    <div class="partner">Meridale</div>
    <div class="partner">Ashgrove Partners</div>
    <div class="partner">Kestrel</div>
  </div>
  <svg width="16" height="40" viewBox="0 0 16 40"><path d="M2 2l12 18L2 38" stroke="#aaa" stroke-width="2" fill="none"/></svg>
</section>

<section class="contact">
  <div class="get-started">
    <h2 class="display">Let's Get <span class="accent">Started</span></h2>
    <p>We're here to help answer your questions. Judicial matters can be complicated, our experts are on hand to help inform you of every aspect regarding your topic. We take great pride in using our expertise for you and look forward to hearing from you.</p>
    <div class="row">
      <div class="field"><div class="ico"><svg width="20" height="20" viewBox="0 0 20 20" fill="#fff"><circle cx="10" cy="6" r="5"/><path d="M1 20c0-6 4-8 9-8s9 2 9 8z"/></svg></div><span>Name*</span></div>
      <div class="field"><div class="ico"><svg width="22" height="16" viewBox="0 0 22 16"><rect width="22" height="16" rx="2" fill="#fff"/><path d="M1 1l10 8 10-8" stroke="#d6435b" stroke-width="2" fill="none"/></svg></div><span>Email*</span></div>
    </div>
    <div class="field"><div class="ico"><svg width="16" height="10" viewBox="0 0 16 10"><path d="M0 0h16L8 10z" fill="#fff"/></svg></div><span>Subjects*</span></div>
    <div class="field tall"><div class="ico"><svg width="22" height="20" viewBox="0 0 22 20" fill="#fff"><ellipse cx="11" cy="8" rx="11" ry="8"/><path d="M4 13l-2 7 7-4z"/></svg></div><span>Message*</span></div>
    <div class="submit">Submit</div>
  </div>
  <div class="contact-us">
    <h2 class="display">Contact <span class="accent">Us</span></h2>
    <div class="info"><span class="pin"><svg width="12" height="16" viewBox="0 0 12 16"><path d="M6 0a6 6 0 0 1 6 6c0 4-6 10-6 10S0 10 0 6a6 6 0 0 1 6-6z" fill="#fff"/></svg></span><div>Norwell &amp; Pike Corporate Office 4410<br>Harbour Lane, Sydney NSW 2000</div></div>
    <div class="info"><span class="pin"><svg width="16" height="16" viewBox="0 0 16 16"><circle cx="8" cy="8" r="6.5" stroke="#fff" stroke-width="2" fill="none"/><path d="M8 4v4h3" stroke="#fff" stroke-width="2" fill="none"/></svg></span><div class="hours"><span>Monday-Friday:</span><span>7am – 7pm</span><span>Saturday:</span><span>10am – 5pm</span><span>Sunday:</span><span>12pm – 4pm</span></div></div>
    <div class="info"><span class="pin"><svg width="14" height="14" viewBox="0 0 14 14"><path d="M2 0l3 3-1.5 2c1 2 3 4 5 5L10.5 8.5 14 11.5 12 14C6 14 0 8 0 2z" fill="#fff"/></svg></span><div class="hours"><span>Corporate Office:</span><span>1-800-555-0190</span><span>Tax Services:</span><span>1-800-555-0171</span><span>International:</span><span>1-800-555-0163</span></div></div>
    <div class="info"><span class="pin"><svg width="14" height="10" viewBox="0 0 14 10"><rect width="14" height="10" fill="#fff"/><path d="M0 0l7 5 7-5" stroke="#d6435b" stroke-width="1.5" fill="none"/></svg></span><div>sales@norwellpike.com<br>support@norwellpike.com<br>office@norwellpike.com</div></div>
    <div class="socials" aria-label="Social links"><span></span><span></span><span></span><span></span></div>
  </div>
</section>

<footer class="footer">©Harcourt Law - 2017 | All Rights Reserved</footer>

</body>
</html>
```